2026 Marlow Smokehouse Jamboree poster design

We need an 11x17 poster made to help sell tickets for a barbecue festival.

I've attached several sample posters, one of them a winning entry from Pixel Harbor.

I've attached a file showing our logo, which should be part of the design. Logo color is flexible.

I've also added logos for the four sponsors mentioned in the specs below.

Symmetrical or asymmetrical designs are both OK.

Source files must be editable (vector, PDF preferred) because lineup change may occur in the future and we will need to update it.

HEADER:
Fernwick by Clay Dorsett presents (smaller text)

13th Annual Marlow Smokehouse Jamboree (Bigger text)
MSJBQ Logo

Tickets
msjbq-fest.com (big text)

Limited availability - All tickets sold in advance - No sales at the door

BODY:

Lot-Z-BBQ
Copper Kin BBQ
Uncle Perkin's BBQ
Windmill Barbecue
Oak Pillar BBQ
Tilbury Lane BBQ
Whitlow & Marsh
Sinchon 58 KBBQ
T-Bow-V Barbecue
El Morral Brand BBQ
Gladwell's Barbecue
Lou's BBQ Hut
Bluejay BBQ
Vantreck Barbecue
Lindqvist Bar-B-Q
Prairie Z BBQ
Rocket Ridge BBQ
Cielo Cocoa & BBQ
The Ember Hall
Slate Porch BBQ
Verdict BBQ
Calloway's Barbecue

FOOTER:
Brixley Commons Pavilion

Sunday - 12 April 2026 - 1pm - 4pm

VIP entry at noon

Our partners (include logos)
Fernwick by Clay Dorsett (this logo should be slightly bigger/more prominent)
Mill Creek Brewing Co.
Corvane Insurance
MSJBQ Guide

festival@msjbq-fest.com - 555.218.7390 - twitter/instagram/tiktok @msjbq - facebook MarlowSmokehouseJamboree

QR Code

RAIN OR SHINE | PARTICIPATING BBQ JOINTS MAY CHANGE WITHOUT NOTICE | COPYRIGHT CHARRED TALLOW LLC

Customers waiting in line at BBQ restaurants will see this poster.

Details of the event from the project description. Source files must be editable (vector) because lineup change may occur in the future and we will need to update it.

Images or graphics of backyard barbecue grills, forks or spatulas. This event features professional restaurants and backyard grilling images don't apply.

Target Market(s)

Industry/Entity Type

Food festival

Requirements
Should not have
• Images or graphics of backyard barbecue grills, forks or spatulas. This event features professional restaurants and backyard grilling images don't apply.

```html
<!DOCTYPE html>
<html lang="en">
<head>
<meta charset="utf-8">
<title>Marlow Smokehouse Jamboree 2026</title>
<link rel="stylesheet" href="https://fonts.googleapis.com/css2?family=Anton&family=Oswald:wght@400;500;600;700&family=Yellowtail&display=swap">
<style>
:root{
  --char:#120806;
  --ember:#3a140a;
  --flame:#e8561a;
  --gold:#f7c21c;
  --amber:#f39a1d;
  --white:#ffffff;
  --ticket:#1f8fd6;
  --ticket-dark:#0f5f9c;
  --date-red:#c8211b;
}
*{margin:0;padding:0;box-sizing:border-box}
html,body{width:727px;height:1200px;overflow:hidden;background:var(--char)}
.poster{position:relative;width:727px;height:1200px;overflow:hidden;font-family:"Oswald",sans-serif;color:var(--white)}
.poster__scene{position:absolute;inset:0;
  background:
    radial-gradient(ellipse 60% 22% at 50% 40%, rgba(214,104,40,.75), transparent 70%),
    radial-gradient(ellipse 70% 18% at 50% 62%, rgba(170,70,25,.55), transparent 75%),
    radial-gradient(ellipse 40% 30% at 0% 95%, rgba(232,86,26,.55), transparent 70%),
    radial-gradient(ellipse 40% 30% at 100% 95%, rgba(232,86,26,.55), transparent 70%),
    radial-gradient(ellipse 30% 20% at 10% 5%, rgba(232,120,30,.5), transparent 70%),
    radial-gradient(ellipse 30% 20% at 90% 5%, rgba(232,120,30,.5), transparent 70%),
    linear-gradient(180deg,#1a0a06 0%,#3a1a0c 35%,#24100a 60%,#140806 100%)}
.header{position:absolute;top:18px;left:0;right:0;text-align:center}
.header__presents{font-family:"Yellowtail",cursive;color:var(--gold);font-size:26px}
.header__annual{font-family:"Anton",sans-serif;font-size:40px;letter-spacing:1px;margin-top:2px;text-shadow:0 2px 6px #000}
.header__title{font-family:"Anton",sans-serif;color:var(--gold);font-size:70px;line-height:1;letter-spacing:1px;text-shadow:0 3px 8px #000}
.header__subtitle{font-family:"Anton",sans-serif;color:var(--white);font-size:46px;line-height:1.05;letter-spacing:2px;text-shadow:0 3px 8px #000}
.brand-mark{position:absolute;top:300px;left:0;right:0;display:flex;justify-content:center;align-items:center;gap:10px}
.brand-mark__dot{width:22px;height:22px;border-radius:50%;background:var(--ticket)}
.brand-mark__name{font-family:"Anton",sans-serif;font-size:34px;color:var(--white)}
.ticket{position:absolute;top:378px;left:50%;transform:translateX(-50%);width:260px;height:92px;background:var(--ticket);border:3px solid var(--white);border-radius:12px;text-align:center;box-shadow:0 4px 14px rgba(0,0,0,.6)}
.ticket__label{font-family:"Anton",sans-serif;font-size:26px;line-height:1;margin-top:10px}
.ticket__url{font-family:"Anton",sans-serif;font-size:30px;line-height:1.2;background:var(--white);color:var(--ticket-dark);margin:6px 14px 0;border-radius:4px}
.notice{position:absolute;top:490px;left:0;right:0;text-align:center;font-weight:700;font-size:17px;color:var(--gold);letter-spacing:.5px;text-shadow:0 2px 4px #000}
.lineup{position:absolute;top:530px;left:24px;right:24px;display:grid;grid-template-columns:repeat(4,1fr);border-top:2px solid var(--flame);border-bottom:2px solid var(--flame);padding:14px 0;background:rgba(10,4,2,.45)}
.lineup__col{list-style:none;padding:0 8px;border-right:1px solid rgba(232,86,26,.7)}
.lineup__col:last-child{border-right:none}
.lineup__joint{font-weight:600;font-size:14.5px;line-height:30px;text-transform:uppercase;color:var(--white);white-space:nowrap}
.lineup__joint:nth-child(even){color:var(--gold)}
.venue{position:absolute;top:800px;left:24px;width:440px}
.venue__name{font-family:"Anton",sans-serif;font-size:50px;line-height:1.02;color:var(--gold);text-transform:uppercase;text-shadow:0 3px 8px #000}
.venue__vip{display:inline-block;margin-top:10px;background:var(--char);border:2px solid var(--flame);padding:4px 14px;font-weight:600;font-size:22px}
.date{position:absolute;top:800px;right:24px;width:220px;background:var(--white);border-radius:8px;text-align:center;padding:10px 0 12px;color:var(--char)}
.date__day{font-family:"Anton",sans-serif;font-size:26px;color:var(--date-red)}
.date__full{font-family:"Anton",sans-serif;font-size:32px;line-height:1.1}
.date__time{font-weight:700;font-size:22px;color:var(--date-red)}
.partners{position:absolute;top:965px;right:24px;width:220px;height:168px;background:rgba(10,4,2,.8);border:2px solid var(--flame);border-radius:10px;padding:8px 12px}
.partners__title{font-family:"Yellowtail",cursive;color:var(--gold);font-size:24px;line-height:1}
.partners__lead{margin-top:8px;height:56px;background:#d9d2c4;border-radius:6px}
.partners__row{display:grid;grid-template-columns:repeat(3,1fr);gap:8px;margin-top:8px}
.partners__badge{height:40px;background:#d9d2c4;border-radius:6px}
.footer{position:absolute;bottom:18px;left:24px;right:24px;font-size:11.5px;line-height:1.6;text-shadow:0 1px 3px #000}
.footer__contact{color:var(--white)}
.footer__legal{color:var(--gold);font-weight:600}
</style>
</head>
<body>
<main class="poster">
  <div class="poster__scene" role="img" aria-label="Photograph of chicken pieces grilling over open flames on a dark background"></div>

  <header class="header">
    <p class="header__presents">Fernwick by Clay Dorsett presents</p>
    <p class="header__annual">13th Annual</p>
    <h1 class="header__title">MARLOW SMOKEHOUSE</h1>
    <p class="header__subtitle">JAMBOREE</p>
  </header>

  <div class="brand-mark">
    <span class="brand-mark__dot"></span>
    <span class="brand-mark__name">MSJBQ</span>
  </div>

  <div class="ticket">
    <p class="ticket__label">Ticket</p>
    <p class="ticket__url">MSJBQ-FEST.COM</p>
  </div>

  <p class="notice">LIMITED AVAILABILITY • ALL TICKETS SOLD IN ADVANCE • NO SALES AT THE DOOR</p>

  <section class="lineup" aria-label="Participating BBQ joints">
    <ul class="lineup__col">
      <li class="lineup__joint">Lot-Z-BBQ</li>
      <li class="lineup__joint">Copper Kin BBQ</li>
      <li class="lineup__joint">Uncle Perkin's BBQ</li>
      <li class="lineup__joint">Windmill Barbecue</li>
      <li class="lineup__joint">Oak Pillar BBQ</li>
    </ul>
    <ul class="lineup__col">
      <li class="lineup__joint">Tilbury Lane BBQ</li>
      <li class="lineup__joint">Whitlow &amp; Marsh</li>
      <li class="lineup__joint">Sinchon 58 KBBQ</li>
      <li class="lineup__joint">T-Bow-V Barbecue</li>
      <li class="lineup__joint">El Morral Brand BBQ</li>
      <li class="lineup__joint">Verdict BBQ</li>
    </ul>
    <ul class="lineup__col">
      <li class="lineup__joint">Gladwell's Barbecue</li>
      <li class="lineup__joint">Lou's BBQ Hut</li>
      <li class="lineup__joint">Bluejay BBQ</li>
      <li class="lineup__joint">Vantreck Barbecue</li>
      <li class="lineup__joint">Lindqvist Bar-B-Q</li>
      <li class="lineup__joint">Calloway's Barbecue</li>
    </ul>
    <ul class="lineup__col">
      <li class="lineup__joint">Prairie Z BBQ</li>
      <li class="lineup__joint">Rocket Ridge BBQ</li>
      <li class="lineup__joint">Cielo Cocoa &amp; BBQ</li>
      <li class="lineup__joint">The Ember Hall</li>
      <li class="lineup__joint">Slate Porch BBQ</li>
    </ul>
  </section>

  <section class="venue">
    <h2 class="venue__name">Brixley Commons Pavilion</h2>
    <p class="venue__vip">VIP entry at noon</p>
  </section>

  <section class="date">
    <p class="date__day">SUNDAY</p>
    <p class="date__full">12 APRIL 2026</p>
    <p class="date__time">1PM – 4PM</p>
  </section>

  <section class="partners" aria-label="Our partners">
    <p class="partners__title">Our Partners</p>
    <div class="partners__lead"></div>
    <div class="partners__row">
      <div class="partners__badge"></div>
      <div class="partners__badge"></div>
      <div class="partners__badge"></div>
    </div>
  </section>

  <footer class="footer">
    <p class="footer__contact">FESTIVAL@MSJBQ-FEST.COM • 555.218.7390 • TWITTER/INSTAGRAM/TIKTOK @MSJBQ • FACEBOOK MARLOWSMOKEHOUSEJAMBOREE</p>
    <p class="footer__legal">RAIN OR SHINE | PARTICIPATING BBQ JOINTS MAY CHANGE WITHOUT NOTICE | COPYRIGHT CHARRED TALLOW LLC</p>
  </footer>
</main>
</body>
</html>
```